Business Card and Stationery for Brokerage & Consulting Co.
Amber Ridge Associates, Brokerage & Consulting for the Baking Industry
Business Card and Stationery for Brokerage & Consulting Co. - Food
Creative Brief
Professional
Derek Halvorsen
Partner / Business Development
4219 W. Birchmont Ave. Long Beach, CA 90714
derek@amberridgeassociates.com

```html
<!DOCTYPE html>
<html lang="en">
<head>
<meta charset="utf-8">
<title>Amber Ridge Associates – Business Card</title>
<link href="https://fonts.googleapis.com/css2?family=Open+Sans:wght@400;600&display=swap" rel="stylesheet">
<style>
  :root {
    --maroon: #4a1a22;
    --maroon-deep: #3a1219;
    --leaf-green: #5b7a2e;
    --paper: #ffffff;
    --ink: #3b3b3b;
    --ink-soft: #6b6b6b;
    --backdrop: #ece8e3;
  }
  * { margin: 0; padding: 0; box-sizing: border-box; }
  html, body {
    width: 1200px; height: 629px; overflow: hidden;
    background: var(--backdrop);
    font-family: "Open Sans", Arial, sans-serif;
  }
  .stage {
    position: relative; width: 1200px; height: 629px;
    display: flex; align-items: center; justify-content: center; gap: 60px;
  }
  .card {
    position: relative; width: 520px; height: 297px;
    box-shadow: 0 6px 18px rgba(0,0,0,0.18);
    overflow: hidden;
  }
  /* Front */
  .card-front {
    background: radial-gradient(ellipse at 50% 45%, var(--maroon) 0%, var(--maroon-deep) 100%);
    display: flex; flex-direction: column; align-items: center; justify-content: center; gap: 14px;
  }
  .brand-dot {
    width: 64px; height: 64px; border-radius: 50%;
    background: var(--paper);
  }
  .brand-name {
    color: var(--paper); font-weight: 600; font-size: 24px; letter-spacing: 0.5px;
  }
  /* Back */
  .card-back { background: var(--paper); }
  .back-brand {
    position: absolute; left: 40px; top: 36px;
    display: flex; align-items: center; gap: 10px;
  }
  .back-brand .brand-dot { width: 34px; height: 34px; background: var(--maroon); }
  .back-brand .brand-name { color: var(--maroon); font-size: 17px; }
  .contact-person {
    position: absolute; left: 40px; top: 118px; width: 230px; text-align: right;
  }
  .person-name { color: var(--leaf-green); font-weight: 600; font-size: 14px; }
  .person-title { color: var(--ink-soft); font-size: 9.5px; margin-top: 3px; }
  .person-address { color: var(--ink-soft); font-size: 9.5px; margin-top: 10px; line-height: 1.5; }
  .divider {
    position: absolute; left: 288px; top: 112px; width: 1px; height: 84px; background: #c9c9c9;
  }
  .contact-list {
    position: absolute; left: 304px; top: 116px; list-style: none;
  }
  .contact-list li {
    display: flex; align-items: center; gap: 8px;
    color: var(--ink); font-size: 9.5px; height: 24px;
  }
  .contact-icon {
    width: 16px; height: 16px; border-radius: 50%; background: var(--maroon);
    display: flex; align-items: center; justify-content: center; flex-shrink: 0;
  }
  .footer-wave { position: absolute; left: 0; bottom: 0; }
</style>
</head>
<body>
<main class="stage">
  <section class="card card-front" aria-label="Business card front">
    <span class="brand-dot"></span>
    <span class="brand-name">Amber Ridge Associates</span>
  </section>

  <section class="card card-back" aria-label="Business card back">
    <div class="back-brand">
      <span class="brand-dot"></span>
      <span class="brand-name">Amber Ridge Associates</span>
    </div>

    <div class="contact-person">
      <p class="person-name">Derek Halvorsen</p>
      <p class="person-title">Partner / Business Development</p>
      <p class="person-address">4219 W. Birchmont Ave.<br>Long Beach, CA 90714</p>
    </div>

    <span class="divider"></span>

    <ul class="contact-list">
      <li>
        <span class="contact-icon">
          <svg width="9" height="9" viewBox="0 0 24 24"><path fill="#fff" d="M6.6 10.8a15 15 0 0 0 6.6 6.6l2.2-2.2a1 1 0 0 1 1-.25 11.4 11.4 0 0 0 3.6.57 1 1 0 0 1 1 1V20a1 1 0 0 1-1 1A17 17 0 0 1 3 4a1 1 0 0 1 1-1h3.5a1 1 0 0 1 1 1c0 1.25.2 2.45.57 3.57a1 1 0 0 1-.25 1z"/></svg>
        </span>562.555.0148
      </li>
      <li>
        <span class="contact-icon">
          <svg width="9" height="9" viewBox="0 0 24 24"><path fill="#fff" d="M2 5h20v14H2z M2 5l10 8 10-8" stroke="#4a1a22" stroke-width="1.5"/></svg>
        </span>derek@amberridgeassociates.com
      </li>
      <li>
        <span class="contact-icon">
          <svg width="9" height="9" viewBox="0 0 24 24"><circle cx="12" cy="12" r="9" fill="none" stroke="#fff" stroke-width="2.5"/><path d="M3 12h18M12 3c3 3 3 15 0 18M12 3c-3 3-3 15 0 18" fill="none" stroke="#fff" stroke-width="1.8"/></svg>
        </span>www.amberridgeassociates.com
      </li>
    </ul>

    <svg class="footer-wave" width="520" height="60" viewBox="0 0 520 60" aria-hidden="true">
      <path d="M0 38 C150 18 330 50 520 22 L520 60 L0 60 Z" fill="var(--leaf-green)"/>
      <path d="M0 30 C150 10 330 42 520 14" fill="none" stroke="var(--maroon)" stroke-width="2"/>
    </svg>
  </section>
</main>
</body>
</html>
```